QT&K PPT

Take my ugly PowerPoint and make it look slick. Use our company color scheme throughout, embed our logo on a couple slides, pick out a couple of stock photos of smiling people and insert where appropriate, and provide multiple slide templates that we can work from. We are launching a new service that is all about reducing time-to-market for medical device manufacturers so include themes relating to medical device, speed, acceleration, overcoming obstacles, and/or breaking down barriers.

```html
<!DOCTYPE html>
<html lang="en">
<head>
<meta charset="utf-8">
<title>QT&amp;K Pre-Validated Packaging Deck</title>
<link href="https://fonts.googleapis.com/css2?family=Roboto:wght@400;500;700&display=swap" rel="stylesheet">
<style>
:root{
  --page:#e6e9f1;
  --slide:#ffffff;
  --blue:#1a72b8;
  --blue-mid:#1f609e;
  --blue-dark:#174c7e;
  --navy:#123d66;
  --ink:#1d1d1f;
  --text:#333a44;
  --muted:#6b7482;
  --line:#d9dee6;
  --card-shadow:0 2px 6px rgba(20,40,70,.14);
}
*{box-sizing:border-box;margin:0;padding:0}
html,body{width:1200px;height:4149px;overflow:hidden;background:var(--page);font-family:"Roboto",Arial,sans-serif;color:var(--text)}
.deck{position:relative;width:1200px;height:4149px}
.slide{position:absolute;left:44px;width:1112px;height:625px;background:var(--slide);overflow:hidden}
.footer{position:absolute;left:0;bottom:0;width:100%;height:27px;background:var(--blue-mid);color:#fff;font-size:11px;display:flex;align-items:center;justify-content:space-between;padding:0 30px}
.footer .mail{display:flex;align-items:center;gap:10px}
.brand{position:absolute;display:flex;align-items:center;gap:8px;color:var(--ink);font-weight:500;line-height:1}
.brand .mark{background:var(--ink)}
.brand.small{right:28px;top:34px;font-size:24px}
.brand.small .mark{width:14px;height:14px}
.brand.large{left:0;width:1112px;justify-content:center;top:62px;font-size:44px;gap:12px}
.brand.large .mark{width:26px;height:26px}
.head-icon{position:absolute;left:29px;top:25px;width:54px;height:54px;border-radius:50%;background:var(--blue);display:flex;align-items:center;justify-content:center}
.head-title{position:absolute;left:99px;top:30px;font-size:32px;font-weight:500;color:var(--ink);line-height:1.35}
.photo{position:absolute}
.hero-title{position:absolute;left:0;width:1112px;text-align:center;top:178px;font-size:48px;font-weight:500;color:var(--ink)}
.hero-circle{position:absolute;width:284px;height:284px;border-radius:50%;display:flex;flex-direction:column;align-items:center;justify-content:center;color:#fff;font-size:28px;font-weight:500;text-align:center;line-height:1.35;border:4px solid #fff}
.hero-circle svg{margin-bottom:14px}
.req-card{position:absolute;top:169px;width:315px;height:364px;background:#fff;box-shadow:var(--card-shadow);border:1px solid #eef0f4}
.req-card .bar{margin-top:37px;height:67px;background:var(--blue-mid);color:#fff;font-size:15px;font-weight:500;display:flex;align-items:center;justify-content:space-between;padding:0 18px;line-height:1.4}
.req-card .bar.dark{background:var(--blue-dark)}
.req-card .bg{position:absolute;left:50%;top:170px;transform:translateX(-50%);width:170px;height:170px;border-radius:50%;background:#e9f1f8;opacity:.8}
.checklist{position:relative;list-style:none;padding:18px 16px 0 18px}
.checklist li{position:relative;padding-left:22px;font-size:15px;line-height:26px;color:var(--text)}
.checklist li::before{content:"";position:absolute;left:0;top:7px;width:10px;height:10px;border:2px solid var(--blue);border-radius:50%}
.checklist li::after{content:"";position:absolute;left:4px;top:10px;width:3px;height:5px;border:solid var(--blue);border-width:0 1.5px 1.5px 0;transform:rotate(40deg)}
.tri-list{position:absolute;left:30px;top:180px;list-style:none}
.tri-list li{position:relative;padding-left:28px;font-size:20px;line-height:43px;color:var(--ink)}
.tri-list li::before{content:"";position:absolute;left:2px;top:16px;border-left:7px solid var(--blue-dark);border-top:5px solid transparent;border-bottom:5px solid transparent}
.panel{position:absolute;top:151px;height:446px;width:556px;color:#fff}
.panel.left{left:0;background:linear-gradient(135deg,#3b8ccb,#2a77b6)}
.panel.right{left:556px;background:var(--blue-mid)}
.panel ul{list-style:none}
.panel .major{position:relative;padding-left:28px;font-size:20px;line-height:28px;margin-top:6px}
.panel .major::before{content:"";position:absolute;left:2px;top:7px;width:11px;height:11px;border:2px solid #fff;border-radius:50%}
.panel .minor{position:relative;padding-left:49px;font-size:16px;line-height:26px}
.panel .minor::before{content:"";position:absolute;left:30px;top:10px;width:5px;height:5px;border:solid #fff;border-width:1.5px 1.5px 0 0;transform:rotate(45deg)}
.intro{position:absolute;left:29px;top:124px;font-size:20px;color:var(--ink)}
.step{position:absolute;top:198px;width:211px;height:266px;background:#fff;box-shadow:var(--card-shadow);border-left:3px solid var(--blue-dark);border-bottom:3px solid var(--blue-dark);border-radius:0 0 0 6px}
.step .num{position:absolute;right:-40px;top:-19px;width:130px;height:116px;color:#fff;font-size:34px;font-weight:500;display:flex;align-items:center;justify-content:center;padding-left:10px}
.step .num svg{position:absolute;inset:0}
.step .num span{position:relative}
.step .icon{position:absolute;left:20px;top:18px}
.step h3{position:absolute;left:20px;top:122px;font-size:18px;font-weight:400;color:var(--ink)}
.step ul{position:absolute;left:20px;top:160px;right:8px;list-style:none}
.step li{position:relative;padding-left:20px;font-size:15px;line-height:27px;color:var(--text)}
.step li::before{content:"";position:absolute;left:2px;top:11px;width:5px;height:5px;border:solid var(--muted);border-width:1.2px 1.2px 0 0;transform:rotate(45deg)}
.down{position:absolute;top:474px}
.pill{position:absolute;top:509px;width:216px;height:54px;background:var(--blue-mid);color:#fff;font-size:17px;font-weight:500;display:flex;align-items:center;justify-content:center}
.note{position:absolute;left:570px;top:505px;width:510px;font-size:17px;font-weight:500;line-height:27px;color:var(--ink)}
.fail-title{position:absolute;left:400px;width:560px;text-align:center;top:238px;font-size:25px;color:var(--ink);white-space:nowrap}
.fail{position:absolute;top:312px;width:150px;text-align:center;font-size:16px;font-weight:500;color:var(--ink)}
.fail .ring{width:84px;height:84px;margin:0 auto 6px;border-radius:50%;background:var(--blue-mid);border:3px solid #fff;box-shadow:0 0 0 2px var(--blue-mid);display:flex;align-items:center;justify-content:center}
</style>
</head>
<body>
<div class="deck">

<section class="slide" style="top:56px">
  <div class="photo" role="img" aria-label="Stacked cardboard shipping boxes fading into the background" style="left:560px;top:0;width:552px;height:598px;background:linear-gradient(100deg,rgba(255,255,255,1) 0%,rgba(240,226,205,.55) 35%,#d9bd95 100%)"></div>
  <div class="brand large"><span class="mark"></span>Halvern Pack</div>
  <h1 class="hero-title">Pre-Validated Packaging</h1>
  <div class="hero-circle" style="left:150px;top:264px;background:var(--blue)">
    <svg width="64" height="64" viewBox="0 0 64 64" fill="none" stroke="#fff" stroke-width="3"><circle cx="32" cy="32" r="28"/><path d="M22 22l20 20M42 22L22 42"/></svg>
    One &amp; Done</div>
  <div class="hero-circle" style="left:414px;top:264px;background:var(--blue-mid)">
    <svg width="64" height="64" viewBox="0 0 64 64" fill="none" stroke="#fff" stroke-width="2.5"><path d="M12 6h30l10 10v40H12z"/><path d="M20 18h18M20 26h24M20 34h10"/><rect x="28" y="38" width="28" height="14" rx="2" fill="#1f609e"/><text x="42" y="49" fill="#fff" stroke="none" font-size="10" font-family="Roboto" font-weight="700" text-anchor="middle">FACT</text></svg>
    Myth vs Reality</div>
  <div class="hero-circle" style="left:676px;top:264px;background:var(--blue-dark)">
    <svg width="64" height="64" viewBox="0 0 64 64" fill="none" stroke="#fff" stroke-width="2.5"><path d="M8 26l24-10 24 10-24 10z"/><path d="M12 28v20l20 9 20-9V28"/><path d="M32 36v21"/><circle cx="32" cy="14" r="8"/><path d="M28 14l3 3 5-6"/></svg>
    Packaging<br>Validation</div>
  <footer class="footer"><span class="mail"><svg width="12" height="9" viewBox="0 0 12 9"><rect width="12" height="9" fill="#fff"/><path d="M0 0l6 5 6-5" stroke="#1f609e" fill="none"/></svg>info@halvernpack.com</span><span>1</span></footer>
</section>

<section class="slide" style="top:733px">
  <div class="head-icon"><svg width="30" height="30" viewBox="0 0 30 30" fill="none" stroke="#fff" stroke-width="2"><path d="M4 10l11-5 11 5-11 5z"/><path d="M4 10v11l11 5 11-5V10M15 15v11"/></svg></div>
  <h2 class="head-title">What is required of a fully Validated<br>Sterile Barrier Packaging System?</h2>
  <div class="brand small"><span class="mark"></span>Halvern Pack</div>
  <div class="req-card" style="left:29px"><div class="bg"></div>
    <div class="bar">Package Design<svg width="24" height="24" viewBox="0 0 24 24" fill="none" stroke="#fff" stroke-width="2"><path d="M4 20L20 4M6 4l14 14M4 8l4-4"/></svg></div>
    <ul class="checklist"><li>Microbial Barrier properties</li><li>Sterilization compatibility</li><li>Box: shelf and shipping carton (protective packaging)</li><li>Biocompatibility/toxicity attributes</li><li>Compatibility of device and package materials</li><li>Compatibility with labeling</li></ul></div>
  <div class="req-card" style="left:400px"><div class="bg"></div>
    <div class="bar dark">Process Validation<svg width="24" height="24" viewBox="0 0 24 24" fill="none" stroke="#fff" stroke-width="2"><circle cx="12" cy="12" r="9"/><path d="M7 12l4 4 8-9"/></svg></div>
    <ul class="checklist"><li>Develop Sealing Parameters</li><li>Sealer IQ, OQ and PQ</li></ul></div>
  <div class="req-card" style="left:768px"><div class="bg"></div>
    <div class="bar">Package Performance Transit<br>Testing<svg width="24" height="24" viewBox="0 0 24 24" fill="none" stroke="#fff" stroke-width="2"><circle cx="12" cy="12" r="9"/><path d="M12 12l5-5"/></svg></div>
    <ul class="checklist"><li>Environmental Conditioning</li><li>Distribution Simulation</li><li>Aging (accelerated &amp; real time)</li><li>Aseptic presentation</li></ul></div>
  <footer class="footer"><span class="mail"><svg width="12" height="9" viewBox="0 0 12 9"><rect width="12" height="9" fill="#fff"/><path d="M0 0l6 5 6-5" stroke="#1f609e" fill="none"/></svg>info@halvernpack.com</span><span>2</span></footer>
</section>

<section class="slide" style="top:1413px">
  <div class="head-icon"><svg width="28" height="28" viewBox="0 0 28 28" fill="none" stroke="#fff" stroke-width="2"><path d="M6 3h12l4 4v18H6z"/><circle cx="17" cy="19" r="4"/></svg></div>
  <h2 class="head-title">What’s available currently on the<br>“Pre-Validated” market?</h2>
  <div class="brand small"><span class="mark"></span>Halvern Pack</div>
  <ul class="tri-list"><li>Generic sterile barrier systems</li><li>Accelerated aging</li><li>Compatible with various sterilization modalities.</li><li>Sealer Validations</li><li>Packaging Materials in stock</li></ul>
  <div class="photo" role="img" aria-label="Hands labeling a cardboard parcel among padded mailers on a dark desk" style="left:696px;top:153px;width:388px;height:324px;background:linear-gradient(135deg,#3a3531,#6b5a45 55%,#2c2825);box-shadow:var(--card-shadow)"></div>
  <div class="photo" role="img" aria-label="Crushed cardboard box" style="left:600px;top:424px;width:266px;height:145px;background:linear-gradient(160deg,#e8cfa6,#c59a62)"></div>
  <div class="photo" role="img" aria-label="Torn and damaged shipping carton" style="left:29px;top:469px;width:175px;height:108px;background:linear-gradient(135deg,#b37a4a,#7a4a27)"></div>
  <footer class="footer"><span class="mail"><svg width="12" height="9" viewBox="0 0 12 9"><rect width="12" height="9" fill="#fff"/><path d="M0 0l6 5 6-5" stroke="#1f609e" fill="none"/></svg>info@halvernpack.com</span><span>3</span></footer>
</section>

<section class="slide" style="top:2093px">
  <div class="head-icon"><svg width="30" height="30" viewBox="0 0 30 30" fill="none" stroke="#fff" stroke-width="2.2"><circle cx="15" cy="15" r="10"/><path d="M12 7a9 9 0 0 1 0 16"/></svg></div>
  <h2 class="head-title">Pre-Validated really means “partially validated”.<br>What is still required?</h2>
  <div class="brand small"><span class="mark"></span>Halvern Pack</div>
  <div class="panel left" role="img" aria-label="Stacked boxes tinted in blue">
    <ul style="position:absolute;left:28px;top:68px">
      <li class="major">Distribution testing</li>
      <li class="minor">Environmental conditioning</li><li class="minor">Distribution simulation</li><li class="minor">Sterile barrier testing</li>
      <li class="major" style="margin-top:10px">Sterilization validation</li>
      <li class="major">Device-specific requirements:</li>
      <li class="minor">Accelerated aging</li><li class="minor">Real-time aging</li><li class="minor">Label design</li>
    </ul>
  </div>
  <div class="panel right">
    <ul style="position:absolute;left:40px;top:68px;width:480px">
      <li class="major">Missing critical components of a ‘World-Class’ packaging system:</li>
      <li class="minor" style="margin-top:12px">Label abrasion test</li><li class="minor">Human factors testing</li><li class="minor">Documentation of process risk assessment</li><li class="minor">Preconfigured shipping carton</li><li class="minor">Submission-ready data set</li>
    </ul>
  </div>
  <footer class="footer"><span class="mail"><svg width="12" height="9" viewBox="0 0 12 9"><rect width="12" height="9" fill="#fff"/><path d="M0 0l6 5 6-5" stroke="#1f609e" fill="none"/></svg>info@halvernpack.com</span><span>4</span></footer>
</section>

<section class="slide" style="top:2771px">
  <div class="head-icon"><svg width="30" height="30" viewBox="0 0 30 30" fill="none" stroke="#fff" stroke-width="2"><path d="M4 8h6l5 7-5 7H4M26 8h-6l-5 7 5 7h6"/></svg></div>
  <h2 class="head-title">How is the timeline affected?</h2>
  <div class="brand small"><span class="mark"></span>Halvern Pack</div>
  <p class="intro">Traditional Packaging Validations take 26 – 30 weeks to complete</p>

  <div class="step" style="left:29px">
    <div class="num"><svg viewBox="0 0 130 116" preserveAspectRatio="none"><path d="M0 0h100l30 58-30 58H0l30-58z" fill="#1f609e"/></svg><span>01</span></div>
    <svg class="icon" width="70" height="64" viewBox="0 0 70 64" fill="none" stroke="#1f609e" stroke-width="2"><rect x="34" y="4" width="24" height="18"/><path d="M14 30l16-16 10 10-16 16zM10 60l4-30M34 60l-10-20M14 44h20"/></svg>
    <h3>Package Design</h3><ul><li>Sterile barrier</li><li>Packaging System</li><li>Labeling</li></ul></div>
  <div class="step" style="left:298px">
    <div class="num"><svg viewBox="0 0 130 116" preserveAspectRatio="none"><path d="M0 0h100l30 58-30 58H0l30-58z" fill="#174c7e"/></svg><span>02</span></div>
    <svg class="icon" width="70" height="64" viewBox="0 0 70 64" fill="none" stroke="#1f609e" stroke-width="2"><path d="M6 4h30l8 8v44H6z"/><path d="M14 20h22M14 28h22M14 36h12"/><circle cx="46" cy="48" r="10"/><path d="M41 48l4 4 6-7"/></svg>
    <h3>Process Validation</h3><ul><li>Sealer settings</li><li>OQ, PQ</li></ul></div>
  <div class="step" style="left:567px">
    <div class="num"><svg viewBox="0 0 130 116" preserveAspectRatio="none"><path d="M0 0h100l30 58-30 58H0l30-58z" fill="#1f609e"/></svg><span>03</span></div>
    <svg class="icon" width="70" height="64" viewBox="0 0 70 64" fill="none" stroke="#1f609e" stroke-width="2"><path d="M4 22h62M35 22v14M24 48l11-12 11 12zM12 48h46"/><circle cx="12" cy="22" r="8"/><circle cx="58" cy="22" r="8"/></svg>
    <h3>Stability Studies</h3><ul><li>Real time aging</li></ul></div>
  <div class="step" style="left:836px">
    <div class="num"><svg viewBox="0 0 130 116" preserveAspectRatio="none"><path d="M0 0h100l30 58-30 58H0l30-58z" fill="#174c7e"/></svg><span>04</span></div>
    <svg class="icon" width="70" height="64" viewBox="0 0 70 64" fill="none" stroke="#1f609e" stroke-width="2"><path d="M24 24l11-5 11 5v14l-11 5-11-5z"/><path d="M35 6v10M35 46v12M12 18l10 6M58 18l-10 6M12 46l10-6M58 46l-10-6"/><circle cx="35" cy="5" r="3"/><circle cx="35" cy="59" r="3"/><circle cx="9" cy="16" r="3"/><circle cx="61" cy="16" r="3"/><circle cx="9" cy="48" r="3"/><circle cx="61" cy="48" r="3"/></svg>
    <h3>Distribution Studies</h3><ul><li>Environmental conditioning</li><li>Transit simulation</li></ul></div>

  <svg class="down" style="left:129px" width="16" height="30" viewBox="0 0 16 30" fill="none" stroke="#444" stroke-width="1.8"><path d="M8 0v28M2 22l6 6 6-6"/></svg>
  <svg class="down" style="left:390px" width="16" height="30" viewBox="0 0 16 30" fill="none" stroke="#444" stroke-width="1.8"><path d="M8 0v28M2 22l6 6 6-6"/></svg>
  <div class="pill" style="left:29px">Pre-Validated</div>
  <div class="pill" style="left:290px">Pre-Validated</div>
  <p class="note">Currently available Pre-Validated packaging eliminates&nbsp; 10 to 12<br>of those weeks</p>
  <footer class="footer"><span class="mail"><svg width="12" height="9" viewBox="0 0 12 9"><rect width="12" height="9" fill="#fff"/><path d="M0 0l6 5 6-5" stroke="#1f609e" fill="none"/></svg>info@halvernpack.com</span><span>5</span></footer>
</section>

<section class="slide" style="top:3451px">
  <div class="photo" role="img" aria-label="Faint stacked cardboard boxes" style="left:560px;top:0;width:552px;height:598px;background:linear-gradient(100deg,rgba(255,255,255,1) 0%,rgba(246,236,222,.7) 45%,#eddcc2 100%)"></div>
  <div class="head-icon"><svg width="30" height="30" viewBox="0 0 30 30" fill="none" stroke="#fff" stroke-width="2"><path d="M4 8h6l5 7-5 7H4M26 8h-6l-5 7 5 7h6"/></svg></div>
  <h2 class="head-title">Potential Failures</h2>
  <div class="brand small"><span class="mark"></span>Halvern Pack</div>
  <div class="step" style="left:29px;top:200px">
    <div class="num"><svg viewBox="0 0 130 116" preserveAspectRatio="none"><path d="M0 0h100l30 58-30 58H0l30-58z" fill="#174c7e"/></svg><span>04</span></div>
    <svg class="icon" width="70" height="64" viewBox="0 0 70 64" fill="none" stroke="#1f609e" stroke-width="2"><path d="M24 24l11-5 11 5v14l-11 5-11-5z"/><path d="M35 6v10M35 46v12M12 18l10 6M58 18l-10 6M12 46l10-6M58 46l-10-6"/><circle cx="35" cy="5" r="3"/><circle cx="35" cy="59" r="3"/><circle cx="9" cy="16" r="3"/><circle cx="61" cy="16" r="3"/><circle cx="9" cy="48" r="3"/><circle cx="61" cy="48" r="3"/></svg>
    <h3>Distribution Studies</h3><ul><li>Environmental conditioning</li><li>Transit simulation</li></ul></div>
  <p class="fail-title">Packages can fail in a variety of ways</p>
  <div class="fail" style="left:440px"><div class="ring"><svg width="46" height="46" viewBox="0 0 46 46" fill="none" stroke="#fff" stroke-width="2"><path d="M6 14l17-8 17 8-17 8z"/><path d="M6 14v18l17 8 17-8V14M23 22v18M28 26l4 4-3 3"/></svg></div>Product Damage</div>
  <div class="fail" style="left:611px"><div class="ring"><svg width="46" height="46" viewBox="0 0 46 46" fill="none" stroke="#fff" stroke-width="2"><path d="M6 28c0 8 34 8 34 0M6 28c0-6 34-6 34 0"/><path d="M16 6v18M23 4v20M30 6v18"/><circle cx="16" cy="6" r="2"/><circle cx="23" cy="4" r="2"/><circle cx="30" cy="6" r="2"/></svg></div>Puncture</div>
  <div class="fail" style="left:759px"><div class="ring"><svg width="46" height="46" viewBox="0 0 46 46" fill="none" stroke="#fff" stroke-width="2"><path d="M6 14l17-8 17 8-17 8z"/><path d="M6 14v18l17 8 17-8V14M23 22v18"/></svg></div>Void</div>
  <div class="fail" style="left:906px"><div class="ring"><svg width="46" height="46" viewBox="0 0 46 46" fill="none" stroke="#fff" stroke-width="2"><rect x="6" y="10" width="28" height="28"/><path d="M15 19l10 10M25 19L15 29M36 6l4-2M37 12l5 0M33 4l1-3"/></svg></div>Creep</div>
  <footer class="footer"><span class="mail"><svg width="12" height="9" viewBox="0 0 12 9"><rect width="12" height="9" fill="#fff"/><path d="M0 0l6 5 6-5" stroke="#1f609e" fill="none"/></svg>info@halvernpack.com</span><span>5</span></footer>
</section>

</div>
</body>
</html>
```